Advertisement Design for Birchwell Apiaries

We sell "green" beekeeping equipment and teach "green" beekeeping classes.
Our message is about organic beekeeping for backyard gardeners.

```html
<!DOCTYPE html>
<html lang="en">
<head>
<meta charset="utf-8">
<title>Birchwell Apiaries – Advertisement</title>
<link href="https://fonts.googleapis.com/css2?family=Tinos:ital,wght@0,400;0,700;1,400&family=Baloo+2:wght@700&family=Kalam:wght@700&family=Libre+Baskerville:wght@700&display=swap" rel="stylesheet">
<style>
  :root {
    --garden-light: #e8e2b8;
    --garden-mid: #9aa36a;
    --garden-deep: #5e6b3c;
    --flower-red: #d9674a;
    --flower-violet: #6a63a8;
    --warm-top: #ffd43b;
    --warm-bottom: #ff9b1e;
    --logo-panel: #e6e6e3;
    --ink: #111111;
    --ink-soft: #3a3a3a;
    --cta-blue: #1f2fb8;
    --cta-magenta: #e020c8;
    --season-red: #ee2a14;
    --eco-green: #2e9a1c;
    --eco-lime: #8cc63f;
    --sign-purple: #4a3d6e;
    --sign-gold: #f7c623;
    --sign-post: #9a9a9a;
    --ribbon-blue: #1c58b8;
    --ribbon-dark: #0e3478;
    --badge-silver: #c9c9c9;
    --star-bronze: #b88a68;
    --mascot-yellow: #f5c842;
    --white: #ffffff;
  }
  * { margin: 0; padding: 0; box-sizing: border-box; }
  html, body { width: 1200px; height: 848px; overflow: hidden; background: var(--white); }
  .ad { position: relative; width: 1200px; height: 848px; overflow: hidden; font-family: "Tinos", serif; }

  .garden-scene {
    position: absolute; left: 0; top: 0; width: 1200px; height: 413px;
    background:
      radial-gradient(ellipse 220px 160px at 150px 260px, rgba(255,255,240,.85), transparent 70%),
      radial-gradient(ellipse 200px 150px at 700px 120px, rgba(255,255,240,.7), transparent 70%),
      linear-gradient(180deg, var(--garden-light) 0%, var(--garden-mid) 45%, var(--garden-deep) 70%, var(--flower-red) 85%, var(--flower-violet) 100%);
  }
  .warm-field {
    position: absolute; left: 0; top: 413px; width: 1200px; height: 435px;
    background: radial-gradient(ellipse 600px 300px at 600px 180px, #ffe36a, transparent 80%),
                linear-gradient(180deg, var(--warm-top) 0%, var(--warm-bottom) 100%);
  }

  .brand-panel {
    position: absolute; left: 0; top: 0; width: 567px; height: 127px;
    background: var(--logo-panel); opacity: .93;
    border-bottom-right-radius: 28px;
    display: flex; align-items: center; gap: 28px; padding-left: 48px;
  }
  .brand-dot { width: 64px; height: 64px; border-radius: 50%; background: var(--ink-soft); flex: none; }
  .brand-name { font-family: "Tinos", serif; font-size: 50px; font-weight: 400; color: var(--ink-soft); white-space: nowrap; }

  .cta-note {
    position: absolute; font-family: "Tinos", serif; font-style: italic; font-size: 38px; line-height: 1; white-space: nowrap;
  }
  .cta-note--blue { left: 677px; top: 98px; color: var(--cta-blue); }
  .cta-note--magenta { left: 112px; top: 261px; color: var(--cta-magenta); }

  .guarantee-seal {
    position: absolute; left: 972px; top: 16px; width: 206px; height: 206px; border-radius: 50%;
    background: radial-gradient(circle, #ececec 0 60%, var(--badge-silver) 61% 100%);
    border: 4px solid #8f8f8f;
  }

  .mascot-star {
    position: absolute; left: 453px; top: 173px; width: 294px; height: 251px; z-index: 2;
    background: radial-gradient(ellipse 70px 80px at 50% 60%, var(--mascot-yellow), transparent 100%),
                radial-gradient(ellipse 140px 125px at 50% 50%, var(--star-bronze), transparent 100%);
  }

  .brand-sign { position: absolute; left: 340px; top: 424px; width: 520px; height: 176px; z-index: 1; }
  .brand-sign__board {
    position: absolute; left: 0; top: 0; width: 520px; height: 80px;
    background: linear-gradient(180deg, #6b5d8f, var(--sign-purple));
    border: 4px solid #bdb6cc; border-radius: 4px;
    display: flex; align-items: center; justify-content: space-between; padding: 4px 12px 0 42px;
    font-family: "Baloo 2", sans-serif; font-size: 38px; color: var(--sign-gold); line-height: 1;
  }
  .brand-sign__post { position: absolute; top: 80px; width: 8px; height: 96px; background: var(--sign-post); }
  .brand-sign__post--left { left: 6px; }
  .brand-sign__post--right { right: 6px; }

  .season-call {
    position: absolute; left: 20px; top: 476px; width: 272px; color: var(--season-red);
    font-family: "Tinos", serif; font-size: 37px; line-height: 56px; text-align: center;
  }

  .main-cta { position: absolute; left: 384px; top: 510px; width: 446px; height: 108px; z-index: 3; }
  .main-cta svg { position: absolute; inset: 0; }
  .main-cta__label {
    position: absolute; inset: 0; display: flex; align-items: center; justify-content: center;
    font-family: "Kalam", cursive; font-weight: 700; font-size: 68px; color: var(--ink); letter-spacing: -1px; padding-top: 8px;
  }

  .eco-building {
    position: absolute; left: 920px; top: 430px; width: 214px; height: 180px;
    background: radial-gradient(ellipse 107px 90px at 50% 50%, var(--eco-lime) 0%, var(--eco-green) 55%, transparent 100%);
  }
  .eco-classes { position: absolute; left: 834px; top: 628px; width: 360px; text-align: center; color: var(--eco-green); font-family: "Libre Baskerville", serif; font-weight: 700; }
  .eco-classes__title { font-size: 38px; line-height: 44px; }
  .eco-classes__sub { font-size: 32px; line-height: 34px; white-space: nowrap; }

  .hive-banner { position: absolute; left: 40px; top: 652px; width: 574px; height: 148px; }
  .hive-banner svg { position: absolute; inset: 0; }
  .hive-banner__label {
    position: absolute; inset: 0; display: flex; align-items: center; justify-content: center;
    font-family: "Tinos", serif; font-weight: 700; font-size: 66px; color: var(--white); padding-top: 6px; white-space: nowrap;
  }

  .welcome-ribbon { position: absolute; left: 676px; top: 708px; width: 520px; height: 130px; }
  .welcome-ribbon svg { position: absolute; inset: 0; }
  .welcome-ribbon__label {
    position: absolute; left: 0; right: 0; top: 24px; text-align: center;
    font-family: "Tinos", serif; font-weight: 700; font-size: 54px; color: var(--white);
    letter-spacing: -1px; text-shadow: 2px 2px 0 var(--ribbon-dark);
  }
</style>
</head>
<body>
<main class="ad">
  <div class="garden-scene" role="img" aria-label="Photograph of a sunlit spring garden with trees and beds of tulips"></div>
  <div class="warm-field"></div>

  <div class="brand-panel">
    <span class="brand-dot"></span>
    <span class="brand-name">Birchwell Apiaries</span>
  </div>

  <p class="cta-note cta-note--blue">call to action</p>
  <p class="cta-note cta-note--magenta">call to action</p>

  <div class="guarantee-seal" role="img" aria-label="Guarantee seal"></div>

  <div class="brand-sign">
    <div class="brand-sign__board"><span>birchwell</span><span>apiaries</span></div>
    <span class="brand-sign__post brand-sign__post--left"></span>
    <span class="brand-sign__post brand-sign__post--right"></span>
  </div>

  <div class="mascot-star" role="img" aria-label="Illustration of a cartoon bee mascot sitting in front of a bronze star"></div>

  <p class="season-call">GET STARTED<br>KEEPING BEES<br>THIS SEASON</p>

  <div class="main-cta">
    <svg width="446" height="108" viewBox="0 0 446 108" aria-hidden="true">
      <path d="M30 26 Q20 4 60 10 Q120 0 200 7 Q300 0 382 9 Q434 7 428 34 Q444 58 424 82 Q430 104 372 100 Q262 108 182 102 Q92 108 46 97 Q6 95 16 69 Q0 48 30 26 Z"
            fill="var(--white)" stroke="var(--ink)" stroke-width="3"/>
    </svg>
    <span class="main-cta__label">call to action</span>
  </div>

  <div class="eco-building" role="img" aria-label="Illustration of a green building standing on green rings"></div>
  <div class="eco-classes">
    <div class="eco-classes__title">GREEN</div>
    <div class="eco-classes__sub">beekeeping classes</div>
  </div>

  <div class="hive-banner">
    <svg width="574" height="148" viewBox="0 0 574 148" aria-hidden="true">
      <path d="M0 18 Q142 0 287 12 Q436 0 574 18 L548 74 L574 130 Q436 112 287 128 Q142 112 0 130 L26 74 Z" fill="var(--ink)"/>
    </svg>
    <span class="hive-banner__label">TOP BAR HIVE</span>
  </div>

  <div class="welcome-ribbon">
    <svg width="520" height="130" viewBox="0 0 520 130" aria-hidden="true">
      <path d="M0 70 L60 60 L70 110 L12 118 L30 92 Z" fill="var(--ribbon-dark)"/>
      <path d="M520 70 L460 60 L450 110 L508 118 L490 92 Z" fill="var(--ribbon-dark)"/>
      <path d="M55 30 Q260 -10 465 30 L455 100 Q260 65 65 100 Z" fill="var(--ribbon-blue)" stroke="#e4ecf8" stroke-width="3"/>
    </svg>
    <span class="welcome-ribbon__label">WELCOME</span>
  </div>
</main>
</body>
</html>
```